Modern Banner and Window Decal Design For Law Firm Lawyer

We are looking for three modern and sophisticated banner design and window decal for our law firm.

Banner measurements/types:

1) Height: 130 cm Width: 160 cm (Outdoor banner)
2) Height: 200 cm Width: 85 cm (Pull up/retractable indoor banner)

Window Decal:
3) Height: 70cm width 70cm

Our law firm is based in Melbourne, Australia and we deal with property law mostly.

We prefer a white background with classic text in black or grey. We would also like a dash of colour so please use a green, blue or aqua colour palette that is consistent with our logo. Vector attached. A nice photo of property, Melbourne city viee, or family home would be nice.

We do not want any law related images - scales of justice, gavel or the like.

Our ultimate goal is to communicate that the firm is modern, professional and knowledgeable

We would like the following:

1. Our logo
2. Our services: - Property Law - Wills - Powers of Attorney - Probate - Estate Administration - Consultancy & Agency
3. Phone number
4. Web Address

5. For pull up/retractable banner we would also like the following text:

We use the latest digital technology and fixed-fees to provide fast and affordable legal advice that is easy to understand.

For privacy reasons, we will provide business details once we have decided on the winner.

We will monitor entries closely and promise to provide feedback and guidance on each entry.

Thank you very much for considering this project.

Target Market(s)

General public, professionals, lawyers and conveyancers

Industry/Entity Type

Law Firm

Font styles to use
Sans Serif

Colors
0393ce
34a6d7
0456a4
3176b5
acd037
33b8a4
86cfc6
00a990
9ccb3b

Requirements
Must have
• 1. Our logo
• 2. Our services: - Property Law - Wills - Powers of Attorney - Probate & Estate Administration - Consultancy & Agency
• 3. Phone number
• 4. Web Address
Nice to have
• Picture of Melbourne, Australia city ; property/buildings/lawyers
Should not have
• We do not want any law related images - scales of justice, gavel or the like.

```html
<!DOCTYPE html>
<html lang="en">
<head>
<meta charset="utf-8">
<title>Kestrel Lawyers – Pull-up Banner</title>
<link href="https://fonts.googleapis.com/css2?family=Montserrat:wght@500;600&family=Roboto+Condensed:wght@400;700&display=swap" rel="stylesheet">
<style>
  :root {
    --stage: #e6e6e6;
    --paper: #f4f4f4;
    --ink: #111111;
    --grey: #555a60;
    --navy: #0456a4;
    --blue: #3176b5;
    --teal: #00a990;
    --aqua: #34a6d7;
  }
  * { margin: 0; padding: 0; box-sizing: border-box; }
  html, body { width: 1200px; height: 1000px; overflow: hidden; }
  body {
    background: var(--stage);
    position: relative;
    font-family: "Montserrat", sans-serif;
  }
  .banner {
    position: absolute;
    left: 412px; top: 36px;
    width: 376px; height: 928px;
    background: var(--paper);
    overflow: hidden;
  }
  .brand {
    position: absolute;
    left: 34px; top: 70px;
    display: flex; align-items: center; gap: 16px;
  }
  .brand-dot {
    width: 84px; height: 84px; border-radius: 50%;
    background: var(--aqua);
  }
  .brand-name {
    color: var(--grey);
    font-weight: 500;
    font-size: 27px;
    line-height: 1.08;
    letter-spacing: 0.5px;
  }
  .scenery {
    position: absolute;
    left: 0; top: 165px;
    width: 376px; height: 500px;
  }
  .services-title {
    position: absolute;
    top: 647px; left: 50%;
    transform: translateX(-50%);
    background: var(--navy);
    color: #fff;
    font-size: 16px; font-weight: 500;
    padding: 3px 12px;
    border-radius: 5px;
    white-space: nowrap;
  }
  .services {
    position: absolute;
    top: 682px; left: 22px; right: 10px;
    list-style: none;
    color: var(--ink);
    font-weight: 600;
    font-size: 16px;
    line-height: 26px;
  }
  .services li { display: flex; align-items: center; }
  .services li::before {
    content: ""; width: 6px; height: 6px;
    background: var(--navy); margin-right: 6px; flex: none;
  }
  .services .pair { gap: 0; }
  .services .pair span + span { margin-left: 32px; display: flex; align-items: center; }
  .services .pair span + span::before {
    content: ""; width: 6px; height: 6px;
    background: var(--navy); margin-right: 6px;
  }
  .tagline {
    position: absolute;
    top: 796px; left: 50px; width: 278px;
    border: 1.5px solid var(--blue);
    border-radius: 4px;
    padding: 4px 4px;
    font-family: "Roboto Condensed", sans-serif;
    font-size: 12px; line-height: 1.35;
    color: var(--ink);
    text-align: center;
  }
  .phone {
    position: absolute;
    top: 852px; left: 0; right: 0;
    display: flex; justify-content: center; align-items: center; gap: 8px;
    font-family: "Roboto Condensed", sans-serif;
    font-weight: 700; font-size: 31px; color: var(--ink);
  }
  .phone-icon {
    width: 26px; height: 26px; border-radius: 5px;
    background: var(--blue);
    display: flex; align-items: center; justify-content: center;
  }
  .web {
    position: absolute;
    top: 892px; left: 0; right: 0;
    text-align: center;
    font-family: "Roboto Condensed", sans-serif;
    font-size: 17px; color: var(--ink);
  }
</style>
</head>
<body>
  <main class="banner">
    <div class="brand">
      <span class="brand-dot"></span>
      <span class="brand-name">KESTREL<br>LAWYERS</span>
    </div>

    <svg class="scenery" viewBox="0 0 376 500" aria-hidden="false">
      <defs>
        <linearGradient id="scene-tone" x1="0" y1="0" x2="0" y2="1">
          <stop offset="0" stop-color="#5d8fd8"/>
          <stop offset="0.35" stop-color="#a9c4ea"/>
          <stop offset="0.5" stop-color="#7f8f8a"/>
          <stop offset="0.62" stop-color="#c9bfb2"/>
          <stop offset="0.75" stop-color="#2f6a9e"/>
          <stop offset="1" stop-color="#245889"/>
        </linearGradient>
      </defs>
      <path class="band-green" d="M0,62 Q190,8 376,28 L376,44 Q190,22 0,78 Z" fill="var(--teal)"/>
      <path class="band-blue" d="M0,78 Q190,22 376,44 L376,80 Q200,40 0,96 Z" fill="var(--navy)"/>
      <path class="photo" role="img" aria-label="Harbour city skyline with boats on the water under a blue sky"
            d="M0,96 Q200,40 376,80 L376,430 Q200,470 0,420 Z" fill="url(#scene-tone)"/>
      <path class="band-blue" d="M0,420 Q200,470 376,430 L376,450 Q200,492 0,446 Z" fill="var(--navy)"/>
      <path class="band-green" d="M0,446 Q200,492 376,450 L376,458 Q200,502 0,460 Z" fill="var(--teal)"/>
    </svg>

    <div class="services-title">OUR SERVICES:</div>
    <ul class="services">
      <li class="pair"><span>PROPERTY LAW</span><span>WILLS</span></li>
      <li>POWERS OF ATTORNEY</li>
      <li>PROBATE &amp; ESTATE ADMINISTRATION</li>
      <li>CONSULTANCY &amp; AGENCY</li>
    </ul>

    <p class="tagline">We use the latest digital technology and fixed-fees to provide fast and affordable legal advice that is easy to understand.</p>

    <div class="phone">
      <span class="phone-icon">
        <svg width="16" height="16" viewBox="0 0 24 24"><path fill="#fff" d="M6.6 10.8a15.1 15.1 0 0 0 6.6 6.6l2.2-2.2a1 1 0 0 1 1-.25 11.4 11.4 0 0 0 3.6.57 1 1 0 0 1 1 1V20a1 1 0 0 1-1 1A17 17 0 0 1 3 4a1 1 0 0 1 1-1h3.5a1 1 0 0 1 1 1c0 1.25.2 2.45.57 3.57a1 1 0 0 1-.25 1z"/></svg>
      </span>
      <span>555-0148-2090</span>
    </div>
    <div class="web">www.kestrellawyers.com</div>
  </main>
</body>
</html>
```